Sales Tip from Ray Castella- Think Like a Buyer-

I am a sales trainer for B2B sales teams. I would like you to create an infographic that my learners can view, easily understand and immediately apply to their day to day work.
The graphic should:
1-Display the title on top- Sales Tip from Ray Castella- Think Like a Buyer
2- Please use the writing and layout from the attachment.
3- Create a tagline at the bottom that says- Top B2B Sales Teams, Sell The Way Thier Clients Buy.
Our company colors are red, silver with slight black trim.
I do not like cartoon like graphics. This must be poweful...
Updates

thank you very much for your consideration. looking forward to seeing your work Ray

Target Market(s)

CEO's of B2B Technology Companies

Font styles to use
Sans Serif

Requirements
Must have
• the apility to attach to a powerpoint slide. company colors...red, silver and a little black
Should not have
• cartoon animation, business,

```html
<!DOCTYPE html>
<html lang="en">
<head>
<meta charset="utf-8">
<title>Sales Tip from Ray Castella – Think Like a Buyer</title>
<link href="https://fonts.googleapis.com/css2?family=Arimo:wght@700&family=Open+Sans:wght@400;700;800&display=swap" rel="stylesheet">
<style>
  :root {
    --red: #e31e25;
    --red-light: #ee7371;
    --red-dark: #d02a26;
    --silver-dark: #4a4a4c;
    --silver-light: #9a9a9c;
    --green: #8cc63f;
    --ink: #111111;
    --ink-soft: #3b3b3d;
    --white: #ffffff;
  }
  * { margin: 0; padding: 0; box-sizing: border-box; }
  html, body { width: 1200px; height: 933px; overflow: hidden; background: var(--white); }
  .infographic {
    position: relative;
    width: 1200px;
    height: 933px;
    font-family: "Open Sans", Arial, sans-serif;
    color: var(--ink);
    overflow: hidden;
  }
  .kicker {
    position: absolute; top: 52px; left: 0; width: 100%;
    text-align: center; font-size: 38px; font-weight: 400; letter-spacing: -0.5px;
  }
  .kicker strong { font-weight: 700; }
  .headline {
    position: absolute; top: 110px; left: 0; width: 100%;
    text-align: center; font-family: "Arimo", Arial, sans-serif;
    font-weight: 700; font-size: 92px; letter-spacing: -2px; color: var(--red);
    line-height: 1;
  }
  .buyer-circle { position: absolute; left: 619px; top: 213px; width: 532px; height: 532px; }
  .column-head {
    position: absolute; top: 242px; height: 71px;
    display: flex; align-items: center; justify-content: center;
    color: var(--white); font-weight: 800; font-size: 33px; letter-spacing: 1.5px;
  }
  .column-head--seller {
    left: 63px; width: 537px;
    background: linear-gradient(100deg, var(--red-light) 0%, #e95a57 55%, var(--red-dark) 100%);
  }
  .column-head--buyer {
    left: 600px; width: 537px;
    background: linear-gradient(100deg, var(--silver-dark) 0%, #6e6e70 50%, var(--silver-light) 100%);
  }
  .rule { position: absolute; height: 2px; background: var(--ink); }
  .rule--seller { left: 137px; width: 463px; }
  .rule--buyer { left: 680px; width: 457px; }
  .num {
    position: absolute; font-family: "Open Sans", Arial, sans-serif;
    font-weight: 700; font-size: 60px; line-height: 1; width: 60px; text-align: center;
  }
  .num--seller { left: 65px; color: var(--red); }
  .num--buyer { left: 616px; color: var(--ink-soft); }
  .item {
    position: absolute; font-size: 23.5px; line-height: 29px; letter-spacing: 0.1px;
  }
  .item--seller { left: 162px; width: 440px; }
  .item--buyer { left: 705px; width: 440px; }
  .tagline {
    position: absolute; top: 765px; left: 0; width: 100%;
    text-align: center; font-weight: 700; font-size: 31px; line-height: 36px;
    letter-spacing: -1.2px; color: var(--ink-soft);
  }
  .base-band { position: absolute; left: 0; bottom: 0; width: 1200px; height: 90px; }
</style>
</head>
<body>
<main class="infographic">
  <p class="kicker">Sales Tip from <strong>Ray Castella</strong></p>
  <h1 class="headline">THINK LIKE A BUYER</h1>

  <svg class="buyer-circle" viewBox="0 0 532 532" aria-hidden="true">
    <circle cx="266" cy="266" r="266" fill="var(--green)"/>
  </svg>

  <div class="column-head column-head--seller">SELLER</div>
  <div class="column-head column-head--buyer">BUYER</div>

  <!-- Seller column -->
  <section class="column column--seller">
    <span class="num num--seller" style="top:332px">1</span>
    <p class="item item--seller" style="top:342px">Do they like us ?</p>
    <div class="rule rule--seller" style="top:388px"></div>

    <span class="num num--seller" style="top:405px">2</span>
    <p class="item item--seller" style="top:398px">Do they like our product or services<br>better than our competition?</p>
    <div class="rule rule--seller" style="top:468px"></div>

    <span class="num num--seller" style="top:481px">3</span>
    <p class="item item--seller" style="top:492px">Will they accept our price ?</p>
    <div class="rule rule--seller" style="top:547px"></div>

    <span class="num num--seller" style="top:561px">4</span>
    <p class="item item--seller" style="top:557px">Can we close it quickly without<br>being too pushy ?</p>
    <div class="rule rule--seller" style="top:628px"></div>
  </section>

  <!-- Buyer column -->
  <section class="column column--buyer">
    <span class="num num--buyer" style="top:332px">1</span>
    <p class="item item--buyer" style="top:325px">How will this impact our<br>business positively ?</p>
    <div class="rule rule--buyer" style="top:388px"></div>

    <span class="num num--buyer" style="top:405px">2</span>
    <p class="item item--buyer" style="top:401px">What risks or disruptions could occur ?<br>How do we mitigate them ?</p>
    <div class="rule rule--buyer" style="top:468px"></div>

    <span class="num num--buyer" style="top:481px">3</span>
    <p class="item item--buyer" style="top:492px">Why do we need to do this now ?</p>
    <div class="rule rule--buyer" style="top:547px"></div>

    <span class="num num--buyer" style="top:561px">4</span>
    <p class="item item--buyer" style="top:573px">Why them and not their competition ?</p>
    <div class="rule rule--buyer" style="top:628px"></div>

    <span class="num num--buyer" style="top:641px">5</span>
    <p class="item item--buyer" style="top:636px">What are all of the costs involved ?<br>Is the price fair market?</p>
    <div class="rule rule--buyer" style="top:708px"></div>
  </section>

  <p class="tagline">The Most Successful B2B Sales Teams<br>Sell The Way That Their Prospects Evaluate and Buy.</p>

  <svg class="base-band" viewBox="0 0 1200 90" preserveAspectRatio="none" aria-hidden="true">
    <defs>
      <linearGradient id="bandRed" x1="0" y1="0" x2="1" y2="0">
        <stop offset="0" stop-color="var(--red-light)"/>
        <stop offset="1" stop-color="var(--red-dark)"/>
      </linearGradient>
    </defs>
    <polygon points="0,14 445,62 0,90" fill="var(--red-light)"/>
    <polygon points="210,90 1200,0 1200,90" fill="url(#bandRed)"/>
  </svg>
</main>
</body>
</html>
```